Invitation - Lumara Holdings Christmas Party 2015

Lumara Holdings Christmas "Block Party" 2015

Brief:
The Lumara Holdings comprises of Lumara, Tesby and KWF. Three separate companies that together offer a complete end to end product development and manufacturing service. We have over 120 employees and we really want to encourage all of them to attend. In years gone by it has been just about going to a bar or restaurant and drinking as much as the staff could. This year we wanted to hold it onsite and get people together with their families to celebrate what we do. We will likely also invite key customers to mingle and enjoy the night. It's going to be held in our car park however the scene will be set with overhead Christmas lights criss crossing the activities below. It's a sort of theme park/block party atmosphere designed to be relaxed and a heap of fun. We will have a DJ playing music all night. Food is from one of Brisbane's best street food vans and we will be running our own wood fired pizza oven all night with the boss cooking up for the staff.

We need an invite that will excite the team and get them to come along. It needs to be classy enough to show what we are trying to achieve with the night and fun enough that the kids can get excited about it too. Heaps of colours and maybe some graphic description of what the nights all about. We will print it on A4 flyers to hand out and also some larger A3 or A2 posters

Event:
We are holding the annual Christmas party this year with a difference. This year it's about getting everyone and their families together. There will be plenty for everyone from the grown ups right down to the little guys.

What's on:

- Full service bar and frozen daiquiris, beer wine and basics
- Brisbane's famous "Chowcart" van will be preparing their amazing gourmet dishes for everyone
- Wood fire pizzas served all night
- Mechanical bull from 5 till 9pm
- Strongman High Striker - prizes to be won
- Door prize raffle entry for each guest
- for the kids there will be a jumping castle (we ordered the giant one incase the big kids wanted to have a go), fairy floss machine and other activities

Times:
4:00-5:00pm - open house, a chance to take your family through the factory to show what we do each day
5:00-9pm - eat, drink and have fun, bring the family and enjoy the night and celebrate a massive year.
RSVP - Friday 23rd October. Strictly by invitation only, Invites are for staff and their immediate families only. All names must be listed on the RSVP as it will be required at the door.

Where : Grand Tent in the car park - 42 Larkspur Lane Hollowfield

When : Sat Nov 7th 4-9pm

PS - it's important that everyone that attends ensures they arrive safely and get home safely, no one should drink and drive and multiple maxi taxis will be available at the end of the night to take people to the city or other nearby locations after the function. Ensure you plan your night well and do not drink and drive. Any food allergies need to be mentioned on your RSVP

Target Market(s)

Staff and their families

Industry/Entity Type

Group

Requirements
Must have
• A really good impact, must get the staff excited and get them to commit to coming along
Nice to have
• It would be great to set the mood in the invite. The lighting on the night will be a major feature. Fairy lights criss crossing the area with the activities below. A bar with hay bales for seating, the mechanical bull in the centre with other activities around the outside. The wood fired pizza over will probably become a place for people to sit and keep warm and the food van parked to one side serving up unreal street food.
Should not have
• No preference

```html
<!DOCTYPE html>
<html lang="en">
<head>
<meta charset="utf-8">
<title>Lumara Holdings Christmas Block Party 2015</title>
<link href="https://fonts.googleapis.com/css2?family=Oswald:wght@300;400;500&family=Open+Sans:wght@400;700&display=swap" rel="stylesheet">
<style>
  :root {
    --red-deep: #a3101c;
    --red-mid: #d8232f;
    --red-glow: #f0525a;
    --bokeh-light: rgba(255, 170, 170, 0.28);
    --bokeh-soft: rgba(255, 120, 120, 0.18);
    --panel: rgba(190, 20, 32, 0.55);
    --panel-line: rgba(255, 200, 200, 0.6);
    --times-panel: rgba(150, 10, 20, 0.55);
    --white: #ffffff;
    --soft-white: #fde6e6;
    --holly-green: #2f7a34;
  }
  * { margin: 0; padding: 0; box-sizing: border-box; }
  html, body { width: 900px; height: 1200px; overflow: hidden; background: #eeeeee; }
  .poster {
    position: relative;
    width: 900px; height: 1200px;
    overflow: hidden;
    color: var(--white);
    font-family: "Oswald", sans-serif;
    text-align: center;
  }
  .poster__backdrop {
    position: absolute; inset: 0;
    background:
      radial-gradient(circle at 12% 18%, var(--bokeh-light) 0 60px, transparent 64px),
      radial-gradient(circle at 30% 8%, var(--bokeh-soft) 0 45px, transparent 49px),
      radial-gradient(circle at 78% 14%, var(--bokeh-light) 0 70px, transparent 74px),
      radial-gradient(circle at 92% 34%, var(--bokeh-soft) 0 55px, transparent 59px),
      radial-gradient(circle at 8% 42%, var(--bokeh-soft) 0 50px, transparent 54px),
      radial-gradient(circle at 60% 30%, var(--bokeh-soft) 0 80px, transparent 84px),
      radial-gradient(circle at 22% 62%, var(--bokeh-light) 0 40px, transparent 44px),
      radial-gradient(circle at 85% 58%, var(--bokeh-light) 0 48px, transparent 52px),
      radial-gradient(circle at 45% 52%, var(--bokeh-soft) 0 65px, transparent 69px),
      radial-gradient(circle at 10% 80%, var(--bokeh-soft) 0 58px, transparent 62px),
      radial-gradient(circle at 70% 78%, var(--bokeh-soft) 0 42px, transparent 46px),
      radial-gradient(circle at 94% 88%, var(--bokeh-light) 0 36px, transparent 40px),
      radial-gradient(circle at 35% 92%, var(--bokeh-soft) 0 50px, transparent 54px),
      radial-gradient(ellipse at 50% 35%, var(--red-glow) 0%, var(--red-mid) 45%, var(--red-deep) 100%);
  }
  .poster__content { position: relative; padding: 52px 60px 0; }
  .title__lead { font-size: 50px; font-weight: 400; letter-spacing: 1px; line-height: 1.1; text-transform: uppercase; }
  .title__main { font-size: 80px; font-weight: 500; line-height: 1.05; text-transform: uppercase; }
  .info-box {
    margin: 0 auto;
    width: 560px;
    background: var(--panel);
    border: 2px solid var(--panel-line);
    padding: 10px 20px 12px;
  }
  .info-box--date { margin-top: 22px; }
  .info-box--place { margin-top: 10px; }
  .date__day { font-size: 46px; font-weight: 400; line-height: 1.1; text-transform: uppercase; }
  .date__day sup { font-size: 24px; }
  .date__time { font-size: 26px; font-weight: 300; line-height: 1.3; }
  .place__name { font-size: 38px; font-weight: 400; line-height: 1.2; text-transform: uppercase; }
  .place__address { font-size: 30px; font-weight: 400; line-height: 1.25; text-transform: uppercase; }
  .whats-on__heading {
    margin: 24px auto 12px;
    width: 540px;
    font-size: 32px; font-weight: 400; line-height: 1.3; text-transform: uppercase;
    display: flex; align-items: center; gap: 18px;
  }
  .whats-on__heading::before, .whats-on__heading::after {
    content: ""; flex: 1; height: 2px; background: var(--panel-line);
  }
  .whats-on__list { list-style: none; width: 560px; margin: 0 auto; }
  .whats-on__list li {
    font-size: 16px; font-weight: 300; line-height: 1.3;
    text-transform: uppercase; letter-spacing: 0.5px;
    margin-bottom: 10px;
  }
  .holly { position: absolute; width: 100px; height: 72px; }
  .holly--left { left: 48px; top: 505px; }
  .holly--right { right: 42px; top: 790px; }
  .times-box {
    margin: 12px auto 0;
    width: 720px;
    background: var(--times-panel);
    padding: 12px 20px 14px;
    font-family: "Open Sans", sans-serif;
    font-size: 11.5px; line-height: 1.45;
    color: var(--soft-white);
  }
  .times-box__title { font-weight: 700; font-size: 13px; margin-bottom: 3px; color: var(--white); }
  .note {
    width: 780px; margin: 16px auto 0;
    text-align: left;
    font-family: "Open Sans", sans-serif;
    font-size: 10.5px; line-height: 1.5;
    color: var(--soft-white);
  }
</style>
</head>
<body>
<main class="poster">
  <div class="poster__backdrop" role="img" aria-label="Soft red background of glowing bokeh Christmas lights"></div>

  <div class="poster__content">
    <header class="title">
      <p class="title__lead">Lumara Holdings Christmas</p>
      <h1 class="title__main">"Block Party" 2015</h1>
    </header>

    <section class="info-box info-box--date">
      <p class="date__day">Sat Nov 7<sup>th</sup></p>
      <p class="date__time">4:00 p.m - 9:00 p.m</p>
    </section>

    <section class="info-box info-box--place">
      <p class="place__name">Grand Tent in the Car Park</p>
      <p class="place__address">42 Larkspur Lane Hollowfield</p>
    </section>

    <section class="whats-on">
      <h2 class="whats-on__heading">What's On</h2>
      <ul class="whats-on__list">
        <li>Full service bar and frozen daiquiris,<br>beer wine and basics</li>
        <li>Brisbane's famous "Chowcart" van will be preparing their<br>amazing gourmet dishes for everyone</li>
        <li>Wood fire pizzas served all night</li>
        <li>Mechanical bull from 5 till 9pm</li>
        <li>Strongman high striker - prizes to be won</li>
        <li>Door prize raffle entry for each guest</li>
        <li>For the kids there will be a jumping castle (we ordered<br>the giant one incase the big kids wanted to have a go),<br>fairy floss machine and other activities</li>
      </ul>
    </section>

    <section class="times-box">
      <p class="times-box__title">Times:</p>
      <p>4:00-5:00pm - open house, a chance to take your family through the factory to show what we do each day.<br>
      5:00-9pm - eat, drink and have fun, bring the family and enjoy the night and celebrate a massive year.<br>
      RSVP - Friday 23rd October. Strictly by invitation only. Invites are for staff and their immediate families only.<br>
      All names must be listed on the RSVP as it will be required at the door.</p>
    </section>

    <p class="note">PS - It's important that everyone that attends ensures they arrive safely and get home safely, no one should drink and drive and multiple maxi taxis will be available at the end of the night to take people to the city or other nearby locations after the function. Ensure you plan your night well and do not drink and drive. Any food allergies need to be mentioned on your RSVP.</p>
  </div>

  <svg class="holly holly--left" viewBox="0 0 100 72" role="img" aria-label="Holly leaves and berries decoration">
    <rect width="100" height="72" rx="28" fill="var(--holly-green)"/>
  </svg>
  <svg class="holly holly--right" viewBox="0 0 100 72" role="img" aria-label="Holly leaves and berries decoration">
    <rect width="100" height="72" rx="28" fill="var(--holly-green)"/>
  </svg>
</main>
</body>
</html>
```